Newsletter Design for Financial Education Videos Startup

Brightpenny is an online resource for those who want to learn more about finance basics - including topics such as retirement, investing, taxes, credit score, savings, and much more! We provide structured online video courses that go into deeper topics such as accounting, calculating taxes, retirement strategies, CPA/CFA overview, etc.
We want a newsletter that really catches the eye and fits the financial-education-for-the-average-person business.
Our newsletter won't have too much content, it will include a video at the top, followed by 3 news headlines with 1-2 sentences explaining the relevance to our subscribers. I've included an example of a template that was created, but it is not at all necessary to stick to that layout - feel free to deviate as much as you want and be creative. Finance seems boring, and that's not us!!
As you can see, our logo is pretty colorful. I'm thinking the colors used for the newsletter should work well with the colors used in our logo (does not have to be the same colors but overall should feel coherent).
Newsletter must work on Mailchimp - HTML code will have to be provided for this.

```html
<!DOCTYPE html>
<html lang="en">
<head>
<meta charset="utf-8">
<title>Brightpenny Newsletter</title>
<link href="https://fonts.googleapis.com/css2?family=Arimo:wght@400;700&family=Carlito:wght@400;700&display=swap" rel="stylesheet">
<style>
  :root {
    --plum: #7b1e5b;
    --plum-deep: #6e1750;
    --orange: #e8581b;
    --ink: #111111;
    --paper: #ffffff;
    --mist: #ececec;
    --rule: #cfcfcf;
  }
  * { box-sizing: border-box; margin: 0; padding: 0; }
  html, body { width: 1200px; height: 3416px; overflow: hidden; background: var(--paper); }
  body { font-family: "Arimo", Arial, sans-serif; color: var(--ink); }
  .newsletter { width: 1200px; height: 3416px; position: relative; }

  .hero { position: relative; height: 600px; background: linear-gradient(160deg, #4b5768 0%, #7a5a3c 45%, #5b2a1e 75%, #2c2220 100%); }
  .brand-box { position: absolute; right: 0; top: 0; width: 348px; height: 160px; background: var(--paper);
    display: flex; align-items: center; justify-content: center; gap: 14px; }
  .brand-dot { width: 34px; height: 34px; border-radius: 50%; background: var(--orange); }
  .brand-name { font-family: "Carlito", "Lato", sans-serif; font-weight: 700; font-size: 44px; color: var(--plum); }

  .tagline { height: 142px; background: var(--plum); color: #fff; font-family: "Carlito", "Lato", sans-serif;
    font-size: 35px; line-height: 46px; text-align: center; display: flex; align-items: center; justify-content: center; }

  .intro { height: 132px; padding-top: 28px; text-align: center; font-weight: 700; font-size: 52px; line-height: 60px; }
  .intro { height: auto; padding: 30px 0 12px; }

  .series-tab { position: relative; height: 86px; width: 600px; }
  .series-tab svg { position: absolute; inset: 0; }
  .series-tab span { position: absolute; left: 32px; top: 14px; color: #fff; font-family: "Carlito", "Lato", sans-serif;
    font-weight: 700; font-size: 46px; }

  .story { position: relative; padding: 0 34px; }
  .story-photo { width: 400px; height: 338px; }
  .story-photo.left { float: left; margin: 0 40px 0 0; }
  .story-photo.right { float: right; margin: 0 0 0 40px; }
  .story-title { font-family: "Carlito", "Lato", sans-serif; font-weight: 700; font-size: 36px; line-height: 44px; color: var(--plum); margin-bottom: 8px; }
  .story-body { font-size: 30.5px; line-height: 38px; text-align: justify; letter-spacing: -0.3px; }
  .story-body p + p { margin-top: 16px; }
  .read-more { clear: both; text-align: right; font-family: "Carlito", "Lato", sans-serif; font-size: 36px; color: var(--plum); padding-right: 36px; }

  .story-one { padding-top: 64px; height: 708px; }
  .story-one .story-title { padding-top: 0; }
  .story-one .read-more { padding-top: 18px; }

  .story-two { background: var(--mist); height: 620px; padding-top: 30px; border-bottom: 2px solid var(--rule); }
  .story-two .story-photo { margin-top: -16px; width: 476px; height: 344px; }
  .story-two .read-more { padding-top: 14px; }

  .story-three { padding-top: 44px; padding-left: 22px; height: 520px; }
  .story-three .story-photo { width: 420px; height: 338px; margin-right: 24px; }
  .story-three .read-more { padding-top: 18px; }

  .signup { position: relative; height: 425px; border-bottom: 2px solid var(--rule); }
  .signup-card { position: absolute; left: 55px; top: 40px; width: 567px; height: 313px; background: var(--orange);
    color: #fff; text-align: center; padding-top: 18px; font-family: "Carlito", "Lato", sans-serif; }
  .signup-card h3 { font-size: 38px; line-height: 44px; }
  .signup-card p { font-size: 26px; line-height: 32px; padding: 6px 40px 0; }
  .signup-button { display: inline-block; margin-top: 18px; background: var(--plum); color: #fff; font-size: 30px;
    padding: 4px 28px; border-radius: 4px; }
  .badges { position: absolute; left: 650px; top: 40px; width: 520px; height: 320px; }

  .footer { height: 156px; background: var(--plum-deep); color: #fff; font-family: "Carlito", "Lato", sans-serif;
    font-size: 24px; line-height: 36px; text-align: center; display: flex; flex-direction: column; justify-content: center; }
</style>
</head>
<body>
<div class="newsletter">

  <header class="hero" role="img" aria-label="Photograph of a business presenter and colleagues around a boardroom table">
    <div class="brand-box"><span class="brand-dot"></span><span class="brand-name">Brightpenny</span></div>
  </header>

  <div class="tagline">25 years of Business, Accounting and Financial<br>Experience with Educational Passion</div>

  <h1 class="intro">Begin your journey to<br>financial knowledge here!</h1>

  <div class="series-tab">
    <svg width="600" height="86" viewBox="0 0 600 86"><polygon points="0,0 555,0 600,43 555,86 0,86" fill="var(--orange)"/></svg>
    <span>Money with Reed</span>
  </div>

  <section class="story story-one">
    <div class="story-photo left" role="img" aria-label="Photograph of a smiling student holding folders with classmates behind" style="background: linear-gradient(135deg,#8fb86a,#c9a0a8 55%,#5e7a48);"></div>
    <h2 class="story-title">BTN Streamly earnings, Drones,<br>ADHD, Marlow Sharks</h2>
    <div class="story-body">
      <p>Every day brings a new development and the big one today is that the Senate bloc abandoned the Health Bill. As discussed yesterday, there were many reasons it was being challenged, and when it got delayed yesterday, it just added up to too much as the bloc lost additional votes. Deal over.</p>
      <p>Streamly reported earnings, and blew through their subscriber estimated. They added over 5 million new subscribers while revenue jumped by about a ⅓. That’s incredible. But you might want to dig a bit deeper. First, understanding subscriber acquisition is a bit of challenge. Programming is doing great with 91 Gala nominations as compared to 54 last year. Interestingly enough.</p>
    </div>
    <div class="read-more">Read More</div>
  </section>

  <section class="story story-two">
    <div class="story-photo right" role="img" aria-label="Photograph of hands working with charts, a calculator and a laptop on a desk" style="background: linear-gradient(135deg,#d7e3ef,#9fb6cf 50%,#e9eef4);"></div>
    <h2 class="story-title">Basic Accounting, Industry</h2>
    <div class="story-body">
      <p>Every day brings a new development and the big one today is that the Senate bloc abandoned the Health Bill. As discussed yesterday, there were many reasons it was being challenged, and when it got delayed yesterday, it just added up to too much as the bloc lost additional votes. Deal over.</p>
      <p>Streamly reported earnings, and blew through their subscriber estimated. They added over 5 million new subscribers while revenue jumped by about a ⅓. That’s incredible. But you might want to dig a bit deeper. First, understanding subscriber acquisition is a bit of challenge. Programming is doing great with 91 Gala nominations as compared to 54 last year. Interestingly enough.</p>
    </div>
    <div class="read-more">Read More</div>
  </section>

  <section class="story story-three">
    <div class="story-photo left" role="img" aria-label="Photograph of hands using a tablet and laptop keyboard" style="background: linear-gradient(135deg,#5a5a5a,#bfbfbf 55%,#2e2e2e);"></div>
    <h2 class="story-title">How the Accounting Industry is Handling<br>Today’s Tech Difficulties</h2>
    <div class="story-body">
      <p>Because of all the evolving technologies and advances that are made in regards to hardware and mechanics, the accounting industry is facing a number of obstacles and changes. These changes in the accounting industry and paving the way for the younger generation of accountants to make their way in the world or business finances. Read on to learn more about the way new accounting technology and advances are changing the face of the accounting world.</p>
    </div>
    <div class="read-more">Read More</div>
  </section>

  <section class="signup">
    <div class="signup-card">
      <h3>With registration, you get...</h3>
      <p>You’ll get access to our content in a course or subject format. You can pick and choose while increasing your knowledge in Business, Accounting and Finance.</p>
      <span class="signup-button">SIGNUP NOW</span>
    </div>
    <svg class="badges" viewBox="0 0 520 320" aria-hidden="true">
      <circle cx="95" cy="75" r="72" fill="#2f5597"/>
      <circle cx="335" cy="75" r="72" fill="#222222"/>
      <rect x="15" y="178" width="195" height="104" fill="#e6c21d"/>
      <rect x="250" y="200" width="230" height="66" fill="#5a5a5a"/>
    </svg>
  </section>

  <footer class="footer">
    <span>Our Website is: www.brightpenny.com</span>
    <span>Copyright@ Current_Year,All rights reserved.</span>
  </footer>

</div>
</body>
</html>
```